Staffing/Recruitment company

We need to upgrade our website. At the moment we have a template that was built last year and looks not good at all.
We would like to update it with a new design based on what is popular this year. Including some visual effects etc.
This website is to give all information to our potential clients about what we do, clients with worked in the past, how to contact us and about us.
The website consists of 4 pages.
We would like to see a design that uses the color blue.
The current website is https://brightkelvo.us/
Logo of the company is uploaded

Some designs were not complete...

```html
<!DOCTYPE html>
<html lang="en">
<head>
<meta charset="utf-8">
<title>Bright Kelvo – About Us</title>
<link href="https://fonts.googleapis.com/css2?family=Poppins:wght@400;500;600;700;800;900&display=swap" rel="stylesheet">
<style>
:root{
  --navy:#0b0a4f;
  --navy-deep:#07063d;
  --orange:#f15a24;
  --orange-soft:#de5a33;
  --grey:#f5f5f5;
  --ink:#1b1a4a;
  --white:#ffffff;
}
*{margin:0;padding:0;box-sizing:border-box}
html,body{width:1200px;height:2367px;overflow:hidden;background:var(--white);font-family:'Poppins',sans-serif;color:var(--ink)}
.page{position:relative;width:1200px;height:2367px;overflow:hidden}
.abs{position:absolute}

/* header */
.site-header{left:0;top:0;width:1200px;height:102px;background:var(--white);z-index:5}
.brand{display:flex;align-items:center;gap:8px;font-weight:700;color:var(--navy);letter-spacing:.2px}
.brand-dot{width:30px;height:30px;border-radius:50%;background:var(--orange)}
.site-header .brand{position:absolute;left:103px;top:36px;font-size:19px}
.nav{position:absolute;top:47px;font-size:12.5px;font-weight:500;color:var(--navy)}
.nav.active{color:var(--orange)}
.btn-contact{position:absolute;left:979px;top:36px;width:110px;height:37px;background:var(--orange);color:var(--white);font-size:12px;font-weight:600;border-radius:3px;display:flex;align-items:center;justify-content:center}

/* hero */
.hero-photo{left:0;top:102px;width:1200px;height:400px;background:radial-gradient(ellipse at 52% 30%,#3a3c78 0%,#1a1960 40%,var(--navy) 75%)}
.hero-title{left:0;top:222px;width:1200px;text-align:center;font-size:66px;font-weight:900;color:var(--white);letter-spacing:-1px}
.hero-sub{left:400px;top:314px;width:400px;text-align:center;font-size:12.5px;line-height:20.5px;color:var(--white)}

/* about */
.about-photo{left:103px;top:581px;width:396px;height:367px;border-radius:6px;background:linear-gradient(135deg,#2c2a2a 0%,#6a5b4e 45%,#a57a58 70%,#4a3a30 100%)}
.about-title{left:645px;top:622px;font-size:42px;font-weight:800;color:var(--navy)}
.accent{color:var(--orange)}
.about-kicker{left:645px;top:685px;font-size:16px;font-weight:500;color:var(--orange)}
.about-copy{left:645px;top:728px;width:460px;font-size:12.5px;line-height:20.6px;color:var(--ink)}
.about-copy p+p{margin-top:20.5px}

/* people */
.people-bg{left:0;top:1040px;width:1200px;height:700px;background:var(--grey)}
.people-title{left:0;top:1144px;width:1200px;text-align:center;font-size:42px;font-weight:800;color:var(--navy);letter-spacing:-.5px}
.people-sub{left:395px;top:1213px;width:410px;text-align:center;font-size:12.5px;line-height:20.6px}
.card{top:1293px;width:305px;height:279px;background:var(--white);border-radius:6px}
.card svg{position:absolute;left:46px;top:26px}
.card h3{position:absolute;left:47px;top:98px;font-size:16px;font-weight:500;color:var(--orange)}
.card p{position:absolute;left:47px;top:141px;width:240px;font-size:12.5px;line-height:20.6px}

/* request */
.req-left{left:0;top:1670px;width:597px;height:550px;background:linear-gradient(180deg,#2a2a72 0%,#1e1d66 40%,#14135a 100%)}
.req-right{left:597px;top:1670px;width:603px;height:550px;background:linear-gradient(180deg,#e0623c 0%,var(--orange-soft) 60%,#d95a32 100%)}
.req-title{left:130px;top:1846px;font-size:42px;font-weight:800;color:var(--white)}
.req-sub{left:133px;top:1909px;width:300px;font-size:12.5px;line-height:20.6px;color:var(--white)}
.contact-icon{width:37px;height:37px;border-radius:50%;background:var(--orange);display:flex;align-items:center;justify-content:center}
.contact-label{font-size:12.5px;color:var(--white)}
.contact-value{font-size:16px;font-weight:600;color:var(--white)}
.field{font-size:12.5px;font-weight:500;color:var(--white);border-bottom:1.5px solid rgba(255,255,255,.85);padding-bottom:3px}
.btn-request{left:962px;top:2044px;width:128px;height:38px;background:var(--white);color:var(--navy);font-size:12.5px;font-weight:500;border-radius:2px;display:flex;align-items:center;justify-content:center}

/* footer */
.social{top:2274px;width:21px;height:21px;border-radius:50%;background:var(--orange)}
.site-footer .brand{position:absolute;left:496px;top:2273px;font-size:17px}
.copyright{left:843px;top:2268px;font-size:12px;font-weight:500;line-height:20px;color:var(--navy-deep)}
</style>
</head>
<body>
<div class="page">

  <header class="abs site-header">
    <div class="brand"><span class="brand-dot"></span>BRIGHT KELVO</div>
    <span class="nav" style="left:708px">Home</span>
    <span class="nav active" style="left:785px">About Us</span>
    <span class="nav" style="left:873px">Clients</span>
    <span class="btn-contact">Contact Us</span>
  </header>

  <section>
    <div class="abs hero-photo" role="img" aria-label="Photo of a businessman in a suit reaching out for a handshake, tinted navy"></div>
    <svg class="abs" style="left:0;top:420px" width="1200" height="90" viewBox="0 0 1200 90">
      <polygon points="0,0 600,62 1200,0 1200,90 0,90" fill="#ffffff"/>
      <polygon points="0,2 600,44 1200,2 1200,4 600,62 0,4" fill="#f15a24"/>
      <polygon points="0,3 600,62 1200,3 1200,5 600,63 0,5" fill="#f15a24"/>
    </svg>
    <h1 class="abs hero-title">WHO WE ARE</h1>
    <p class="abs hero-sub">Day in and day out for the last years we’ve been more than just a staffing company.</p>
  </section>

  <section>
    <div class="abs about-photo" role="img" aria-label="Photo of colleagues at a wooden meeting table taking notes"></div>
    <h2 class="abs about-title">ABOUT <span class="accent">US</span></h2>
    <div class="abs about-kicker">Who We Are</div>
    <div class="abs about-copy">
      <p>Day in and day out for the last years we’ve been more than just a staffing company. Throughout this time we’ve built relationships, we’ve grown together internally and externally, and have created a system that allows us to personally cater to the needs of our clients and candidates.</p>
      <p>We’ve been a mentor for some, a team builder for others, but most importantly we’ve been there. We know there is no substitute for experience, so let us help you navigate through the ever changing web of talent.</p>
    </div>
  </section>

  <section>
    <div class="abs people-bg"></div>
    <svg class="abs" style="left:0;top:1038px" width="1200" height="66" viewBox="0 0 1200 66">
      <polygon points="0,62 600,0 1200,62" fill="#f15a24"/>
      <polygon points="0,66 600,16 1200,66" fill="#f5f5f5"/>
    </svg>
    <h2 class="abs people-title"><span class="accent">MEET</span> OUR PEOPLE</h2>
    <p class="abs people-sub">Day in and day out for the last years we’ve been more than just a staffing company.</p>

    <article class="abs card" style="left:103px">
      <svg width="54" height="54" viewBox="0 0 54 54" fill="none" stroke="#0b0a4f" stroke-width="1.8">
        <path d="M14 4h14l-3 7h-8z"/><path d="M17 11C6 18 2 30 4 40c2 8 10 10 18 10h6"/>
        <path d="M25 11c4 3 7 7 9 11"/><circle cx="20" cy="35" r="7"/>
        <rect x="30" y="22" width="20" height="28" rx="2"/><rect x="33" y="25" width="14" height="6"/>
        <path d="M34 36h3M40 36h3M34 41h3M40 41h3M34 46h3M40 46h3"/>
      </svg>
      <h3>Finance</h3>
      <p>With Wall Street’s fast-paced dynamic and ever-changing environment , business demands are always transforming for new and the best talent.</p>
    </article>

    <article class="abs card" style="left:448px">
      <svg width="56" height="54" viewBox="0 0 56 54" fill="none" stroke="#0b0a4f" stroke-width="1.8">
        <path d="M20 8V3h16v5"/><rect x="2" y="8" width="52" height="40" rx="2"/>
        <path d="M2 16l26 16 26-16"/><circle cx="28" cy="26" r="9"/><circle cx="28" cy="24" r="3"/>
        <path d="M22 32c2-4 10-4 12 0"/>
      </svg>
      <h3>Healthcare</h3>
      <p>Not only do we provide services to the finance and technology world<br>we also service the healthcare industry with IT professionals as well.</p>
    </article>

    <article class="abs card" style="left:794px">
      <svg width="56" height="54" viewBox="0 0 56 54" fill="none" stroke="#0b0a4f" stroke-width="1.8">
        <path d="M4 14L28 3l24 11z"/><rect x="4" y="14" width="48" height="5"/>
        <rect x="8" y="19" width="8" height="24"/><rect x="40" y="19" width="8" height="24"/>
        <path d="M16 24h24"/><rect x="2" y="43" width="52" height="6"/>
      </svg>
      <h3>Government Projects</h3>
      <p>Navigating the rules and regulations of Government integrators<br>isn’t always easy. Our government division, BKGov, recognizes the demands</p>
    </article>
  </section>

  <section>
    <div class="abs req-left" role="img" aria-label="Photo of an empty conference room with office chairs, tinted navy"></div>
    <div class="abs req-right" role="img" aria-label="Photo of an empty conference room with office chairs, tinted orange"></div>
    <svg class="abs" style="left:0;top:1664px" width="1200" height="80" viewBox="0 0 1200 80">
      <polygon points="0,73 600,6 1200,73 1200,0 0,0" fill="#f5f5f5"/>
      <polygon points="0,73 600,6 1200,73 1200,75 600,20 0,75" fill="#0b0a4f"/>
      <polygon points="0,73 600,6 1200,73 600,22" fill="#0b0a4f"/>
    </svg>
    <h2 class="abs req-title">REQUEST A CALL</h2>
    <p class="abs req-sub">Request a call from us to discuss our services and price estimation</p>

    <div class="abs contact-icon" style="left:136px;top:1980px">
      <svg width="16" height="20" viewBox="0 0 16 20" fill="none" stroke="#fff" stroke-width="1.8"><path d="M8 19S1 11 1 7a7 7 0 0 1 14 0c0 4-7 12-7 12z"/><circle cx="8" cy="7" r="2.5"/></svg>
    </div>
    <div class="abs contact-label" style="left:190px;top:1978px">Address</div>
    <div class="abs contact-value" style="left:190px;top:1997px">2140 Harbor Ave, Linden, VA</div>

    <div class="abs contact-icon" style="left:136px;top:2059px">
      <svg width="20" height="15" viewBox="0 0 20 15" fill="none" stroke="#fff" stroke-width="1.8"><rect x="1" y="1" width="18" height="13" rx="2"/><path d="M1 3l9 6 9-6"/></svg>
    </div>
    <div class="abs contact-label" style="left:190px;top:2058px">Email Address</div>
    <div class="abs contact-value" style="left:190px;top:2077px">info@brightkelvo.us</div>

    <div class="abs field" style="left:662px;top:1867px;width:186px">First Name</div>
    <div class="abs field" style="left:886px;top:1867px;width:203px">Last Name</div>
    <div class="abs field" style="left:662px;top:1919px;width:186px">Email address</div>
    <div class="abs field" style="left:886px;top:1919px;width:203px">Phone</div>
    <div class="abs field" style="left:662px;top:1979px;width:427px;padding-bottom:14px">Message</div>
    <div class="abs btn-request">Request</div>
  </section>

  <footer class="site-footer">
    <span class="abs social" style="left:146px"></span>
    <span class="abs social" style="left:181px"></span>
    <span class="abs social" style="left:217px"></span>
    <span class="abs social" style="left:253px"></span>
    <span class="abs social" style="left:289px"></span>
    <div class="brand"><span class="brand-dot"></span>BRIGHT KELVO</div>
    <div class="abs copyright">© 2022 Copyright: <span class="accent">Bright Kelvo, LLC</span><br>All rights reserved</div>
  </footer>

</div>
</body>
</html>
```